Improving a camping website homepage header*

My client is very happy with his new website and its new functionalities. However, he's not very happy about the homepage design. Specifically, the header(this includes the menu, large header image and two columns beneath that). You can find the website here: http://lnkvo.example/siteTentra .

He forwarded me several other websites he likes. Which can be found in the attachments. I also included several pictures of the camping.

I'm looking for a design that will improve the header of the homepage with room for other global style chances. The logo cannot be changed.

Attachments
1) His old website homepage
2) Website mockup he liked.
3) Another website mockup he liked.

Other images can be found on the new website http://lnkvo.example/siteTentra or his old website http://lnkvo.example/formerSiteTentra.

Can you help us?
Updates

Hello guys. Here's a bit more information - Language used on the website is dutch. - The two columns left/right are supposed to link to Hire/Buy chalets. The client indicated that he finds these links important, but doesn't like the current design. I think this is partially the case because he doesn't like the icons. I'm looking forward to your designs!

Target Market(s)

30-50 year old wealthy people that want to purchase or rent cabins in the Netherlands.

Number of Pages Required

1 page

Colors

Designer to choose colors to be used in the design.

Requirements
Must have
• Improved header
Nice to have
• Global style changes
Should not have
• Logo changes

```html
<!DOCTYPE html>
<html lang="nl">
<head>
<meta charset="utf-8">
<title>Parc Lindewaard – Home</title>
<link rel="stylesheet" href="https://fonts.googleapis.com/css2?family=Open+Sans:wght@400;600;700&display=swap">
<style>
:root{
  --green:#84c100;
  --green-dark:#6c9f00;
  --orange:#e58a0b;
  --orange-soft:#f4c58c;
  --blue:#2aa7df;
  --ink:#222;
  --text:#444;
  --muted:#8a8a8a;
  --line:#e6e6e6;
  --white:#fff;
}
*{box-sizing:border-box;margin:0;padding:0}
html,body{width:1120px;height:1200px;overflow:hidden;background:var(--white)}
body{position:relative;font-family:"Open Sans",sans-serif;color:var(--text)}
.abs{position:absolute}

/* top bar */
.topbar{left:0;top:0;width:1120px;height:30px;background:var(--green)}
.topbar-phone{left:128px;top:0;height:30px;display:flex;align-items:center;gap:10px;color:var(--white);font-size:11px;font-weight:600;white-space:nowrap}
.topbar-mail{left:826px;top:8px}
.topbar-chat{left:864px;top:6px;width:18px;height:18px;border-radius:50%;background:var(--white)}
.login{left:902px;top:0;width:112px;height:30px;background:var(--orange);color:var(--white);font-size:11px;font-weight:600;display:flex;align-items:center;justify-content:center;white-space:nowrap}

/* navigation */
.navbar{left:0;top:30px;width:1120px;height:76px;background:var(--white)}
.brand{left:124px;top:44px;display:flex;align-items:center;gap:10px}
.brand-mark{width:30px;height:30px;border-radius:50%;background:var(--green)}
.brand-name{font-size:20px;font-weight:600;color:var(--green-dark);white-space:nowrap}
.menu{left:390px;top:30px;height:76px;display:flex;list-style:none}
.menu li{height:76px;display:flex;align-items:center;padding:0 16px;font-size:13.6px;color:#333;position:relative;white-space:nowrap}
.menu li.active{color:var(--green)}
.menu li.active::after{content:"";position:absolute;left:0;right:0;bottom:0;height:6px;background:var(--green)}

/* hero */
.hero{left:0;top:106px;width:1120px;height:437px;
  background:linear-gradient(180deg,#b9c9cf 0%,#5d7a4a 20%,#3f6a7a 45%,#557f8c 62%,#9a9474 80%,#6f8f3c 100%)}
.hero-shade{left:124px;top:170px;width:354px;height:257px;background:rgba(40,40,40,.62)}
.hero-title{left:0;top:219px;width:392px;height:79px;background:var(--green-dark);color:var(--white);font-size:34px;font-weight:700;display:flex;align-items:center;padding-left:30px;white-space:nowrap;overflow:hidden}
.hero-text{left:156px;top:314px;width:300px;color:var(--white);font-size:13px;font-weight:700;line-height:18.4px}
.hero-rule{left:510px;top:320px;width:98px;height:2px;background:var(--white)}
.dots{left:523px;top:472px;display:flex;gap:16px}
.dots span{width:13px;height:13px;border-radius:50%;background:var(--white)}
.dots span.on{background:var(--green)}

/* feature cards */
.feature{top:512px;width:414px;height:221px;background:var(--white);box-shadow:0 4px 12px rgba(0,0,0,.08)}
.feature-photo{left:18px;top:26px;width:145px;height:172px}
.feature h2{position:absolute;left:192px;top:20px;font-size:25px;font-weight:700;color:var(--ink);letter-spacing:.4px;white-space:nowrap}
.feature p{position:absolute;left:194px;top:63px;width:212px;font-size:12.6px;line-height:15.4px;color:#222}
.btn{position:absolute;left:194px;top:161px;width:148px;height:37px;background:var(--orange);color:var(--white);font-size:13.6px;font-weight:700;display:flex;align-items:center;justify-content:center}

/* listings */
.section-title{left:75px;top:784px;font-size:24px;font-weight:400;color:#333}
.listing{top:830px;width:305px;height:364px;border:1px solid var(--line);background:var(--white)}
.listing-photo{left:0;top:0;width:303px;height:190px}
.tag{position:absolute;top:19px;height:16px;padding:0 6px;font-size:10.5px;display:flex;align-items:center}
.tag-featured{left:18px;background:var(--orange-soft);color:#5a3a10}
.tag-rent,.tag-buy{right:18px;background:var(--blue);color:var(--white)}
.tag-sold{right:18px;color:var(--white);font-weight:600}
.photo-count{position:absolute;right:18px;top:166px;color:var(--white);font-size:11px;display:flex;gap:3px;align-items:center}
.listing h3{position:absolute;left:18px;top:206px;font-size:16px;font-weight:400;color:#333}
.price{position:absolute;left:18px;top:234px;font-size:15px;color:var(--orange)}
.desc{position:absolute;left:18px;top:264px;font-size:11.5px;color:#777}
.meta{position:absolute;left:18px;display:flex;gap:12px;font-size:11px;color:#888;align-items:center;white-space:nowrap}
.meta i{display:inline-block;width:14px;height:8px;border:1.4px solid #b8c2d0;border-top-width:0;margin-right:4px;vertical-align:middle}
.more{position:absolute;right:18px;height:16px;padding:0 6px;background:var(--orange-soft);color:var(--white);font-size:10.5px;display:flex;align-items:center}
.divider{position:absolute;left:18px;right:18px;top:314px;height:1px;background:var(--line)}
.author{position:absolute;left:18px;top:326px;display:flex;align-items:center;gap:10px;font-size:12px;color:#777}
.avatar{width:26px;height:26px;border-radius:50%;background:#7c8a6a}
.avatar.blank{background:#d4d4d4}
.actions{position:absolute;right:18px;top:327px;display:flex;gap:5px}
.actions span{width:26px;height:26px;border:1px solid var(--line);display:flex;align-items:center;justify-content:center;color:#b8c2d0;font-size:13px}
</style>
</head>
<body>

<div class="abs topbar"></div>
<div class="abs topbar-phone">
  <svg width="14" height="14" viewBox="0 0 24 24"><path fill="#fff" d="M6.6 10.8a15.1 15.1 0 0 0 6.6 6.6l2.2-2.2c.3-.3.7-.4 1-.2 1.1.4 2.300.6 3.6.6.6 0 1 .4 1 1V20c0 .6-.4 1-1 1A17 17 0 0 1 3 4c0-.6.4-1 1-1h3.5c.6 0 1 .4 1 1 0 1.3.2 2.5.6 3.6.1.3 0 .7-.2 1z"/></svg>
  Call us today : 0312 - 40 22 17
</div>
<svg class="abs topbar-mail" width="20" height="14" viewBox="0 0 20 14"><rect width="20" height="14" fill="#fff"/><path d="M0 0l10 8 10-8" fill="none" stroke="#84c100" stroke-width="1.6"/></svg>
<div class="abs topbar-chat"></div>
<div class="abs login">Login / Sign up</div>

<div class="abs navbar"></div>
<div class="abs brand"><span class="brand-mark"></span><span class="brand-name">Parc Lindewaard</span></div>
<ul class="abs menu">
  <li class="active">Home</li><li>Hetpark</li><li>Financiering</li><li>Chalets</li><li>Aanbidingen</li><li>Faciliteiten</li><li>Contact</li>
</ul>

<div class="abs hero" role="img" aria-label="Foto van het meer in het park met chalets aan de oever, strand en parasols"></div>
<div class="abs hero-shade"></div>
<div class="abs hero-title">PARC LINDEWAARD</div>
<p class="abs hero-text">Lorem ipsum dolor sit amet, consectetur adip-iscing elit. Aeneaneuismod bibendum laoreet. Proin gravida dolor sit amet lacus accumsan et viverra justo commodo.</p>
<div class="abs hero-rule"></div>
<div class="abs dots"><span class="on"></span><span></span><span></span></div>

<section class="abs feature" style="left:128px">
  <div class="abs feature-photo" role="img" aria-label="Foto van een wit huurchalet" style="background:linear-gradient(160deg,#c9d3dc,#9aa3a8 55%,#5f7a45)"></div>
  <h2>CHALET HUREN</h2>
  <p>Lorem ipsum dolor sit amet, con-sectetur adipiscing elit. Aenean euismod bibendum laoreet. Proin gravida dolor sit amet lacus accumsan.</p>
  <span class="btn">HIRE NOW</span>
</section>
<section class="abs feature" style="left:552px">
  <div class="abs feature-photo" role="img" aria-label="Foto van een crèmekleurig chalet te koop in het groen" style="background:linear-gradient(160deg,#8fa86a,#d8dccf 50%,#5e8a2e)"></div>
  <h2>CHALET KOPEN</h2>
  <p>Lorem ipsum dolor sit amet, con-sectetur adipiscing elit. Aenean euismod bibendum laoreet. Proin gravida dolor sit amet lacus accumsan.</p>
  <span class="btn">BUY NOW</span>
</section>

<h2 class="abs section-title">Recente Chalets</h2>

<article class="abs listing" style="left:75px">
  <div class="abs listing-photo" role="img" aria-label="Foto van chalet Kavel 190 met terras" style="background:linear-gradient(170deg,#b7c8d6,#8d969c 45%,#4f6b33)"></div>
  <span class="tag tag-featured">Aanbevolen</span><span class="tag tag-rent">Huren</span>
  <span class="photo-count">&#9635; 1</span>
  <h3>Kavel 190</h3>
  <div class="price">€ 350 per maand</div>
  <div class="meta" style="top:276px"><span><i></i>1</span><span><i></i>3</span><span><i></i>105 000,00 m²</span></div>
  <span class="more" style="top:272px">lees meer</span>
  <div class="divider"></div>
  <div class="author"><span class="avatar"></span>admin</div>
  <div class="actions"><span>&lt;</span><span>&#9829;</span><span>+</span></div>
</article>

<article class="abs listing" style="left:408px">
  <div class="abs listing-photo" role="img" aria-label="Foto van chalet Kavel 233 aan het water" style="background:linear-gradient(170deg,#8fa874,#c9cdc0 45%,#4c7a25)"></div>
  <span class="tag tag-featured">Aanbevolen</span><span class="tag tag-buy" style="right:94px">Kopen</span><span class="tag tag-sold">Verkocht</span>
  <span class="photo-count">&#9635; 1</span>
  <h3>Kavel 233</h3>
  <div class="price">€ 205.000</div>
  <div class="desc">Ook een mooie chalet.</div>
  <div class="meta" style="top:295px"><span><i></i>1</span><span><i></i>1</span><span><i></i>130,00 m²</span></div>
  <span class="more" style="top:291px">lees meer</span>
  <div class="divider"></div>
  <div class="author"><span class="avatar"></span>admin</div>
  <div class="actions"><span>&lt;</span><span>&#9829;</span><span>+</span></div>
</article>

<article class="abs listing" style="left:740px">
  <div class="abs listing-photo" role="img" aria-label="Foto van houten blokhutten Kavel 236" style="background:linear-gradient(170deg,#c4ccd4,#a4622e 45%,#5a4a3a)"></div>
  <span class="tag tag-featured">Aanbevolen</span><span class="tag tag-buy">Kopen</span>
  <svg class="abs" style="left:18px;top:84px" width="12" height="24" viewBox="0 0 12 24"><path d="M11 1L1 12l10 11" fill="none" stroke="#fff" stroke-width="1.6"/></svg>
  <svg class="abs" style="right:18px;top:84px" width="12" height="24" viewBox="0 0 12 24"><path d="M1 1l10 11L1 23" fill="none" stroke="#fff" stroke-width="1.6"/></svg>
  <span class="photo-count">&#9654; &#9635; 3</span>
  <h3>Kavel 236</h3>
  <div class="price">€ 195.000</div>
  <div class="desc">Prachtige locatie incl. video!</div>
  <div class="meta" style="top:295px"><span><i></i>3</span><span><i></i>2</span><span><i></i>100,00 m²</span></div>
  <span class="more" style="top:291px">lees meer</span>
  <div class="divider"></div>
  <div class="author"><span class="avatar blank"></span>Naam Achternaam</div>
  <div class="actions"><span>&lt;</span><span>&#9829;</span><span>+</span></div>
</article>

</body>
</html>
```